Veltrano Community Development Planning New web site

Design a new web site. I have a budget of $1,500.00.
Attached on PowerPoint is a complete site plan. Home page and linked pages.
10 - 12 pages. All copy and photos will be supplied. (300dpi)
I have shown them the concept which they like.
No data bases required. Home page with animations dissolving.
They former web site has been taken down. They have been in business 30 years in New Jersey
Colors teal blues and greens
There will be a new logo)being designed)
The text in home page copy will give you a detailed story what they are all about.

files have been approved for Veltrano, Inc.   Tomas is the designer

Industry/Entity Type

Community

```html
<!DOCTYPE html>
<html lang="en">
<head>
<meta charset="utf-8">
<title>Veltrano, Inc. — Community Development Planning</title>
<link href="https://fonts.googleapis.com/css2?family=Raleway:wght@300;400;800&family=Roboto:wght@300;400;500;700&family=Signika:wght@600&display=swap" rel="stylesheet">
<style>
:root{
  --green:#35b566;
  --green-dark:#2a9a55;
  --orange:#f7931e;
  --ink:#222;
  --text:#555;
  --light:#f3f3f3;
  --dark:#3a3a3a;
  --footer:#111;
}
*{margin:0;padding:0;box-sizing:border-box}
html,body{width:749px;height:1200px;overflow:hidden}
body{position:relative;background:#fff;font-family:"Roboto",sans-serif;color:var(--text)}
.abs{position:absolute}

/* header */
.site-header{left:0;top:0;width:749px;height:77px;border-bottom:2px solid var(--green);background:#fff}
.brand{left:75px;top:32px;display:flex;align-items:center;gap:6px}
.brand-mark{width:12px;height:12px;background:var(--green)}
.brand-name{font-family:"Raleway",sans-serif;font-weight:800;font-size:22px;color:var(--ink)}
.contact-line{top:17px;display:flex;align-items:center;gap:6px;font-weight:500;font-size:13px;color:var(--green)}
.contact-divider{left:541px;top:13px;width:1px;height:24px;background:#ccc}
.main-nav{left:266px;top:52px;display:flex;align-items:center;font-size:9.5px;color:var(--ink)}
.main-nav a{color:inherit;text-decoration:none;padding:0 7px;border-left:1px solid #ccc;line-height:10px}
.main-nav a.current{background:var(--green);color:#fff;border:none;line-height:24px;padding:0 4px}
.main-nav a.current + a{border-left:none}

/* hero */
.hero{left:0;top:77px;width:749px;height:313px;background:linear-gradient(90deg,#fafafa 0%,#f1f1f1 45%,#e9edf2 100%)}
.hero-visual{left:400px;top:77px;width:349px;height:313px;background:radial-gradient(ellipse at 65% 40%,#cfdcec 0%,#e5ebf2 55%,#eef0f3 100%)}
.hero-intro{left:77px;top:160px;font-family:"Raleway",sans-serif;font-weight:400;font-size:29px;color:var(--ink)}
.hero-line{font-family:"Raleway",sans-serif;font-weight:800;color:var(--green);font-size:21.5px;letter-spacing:-.3px}
.hero-amp{left:73px;top:215px;font-family:"Raleway",sans-serif;font-weight:800;font-size:52px;color:var(--ink);line-height:1}
.hero-sub{left:114px;top:256px;font-family:"Raleway",sans-serif;font-weight:800;font-size:11.5px;color:var(--ink)}
.cta{left:74px;top:291px;width:165px;height:32px;background:var(--orange);color:#fff;font-size:14px;font-weight:500;display:flex;align-items:center;justify-content:center;border-radius:2px;letter-spacing:.3px}

/* service tiles */
.tile{top:414px;width:147px;height:100px;background:linear-gradient(160deg,#4d5a47 0%,#2f3a2f 60%,#3b4236 100%);border-bottom:4px solid var(--orange);color:#f0f0f0;display:flex;flex-direction:column;align-items:center;justify-content:center;text-align:center;font-weight:300;font-size:14.5px;line-height:1.3}
.tile small{font-size:8px;line-height:1.4;display:block}

/* about */
.about{left:0;top:536px;width:749px;height:328px;background:var(--light)}
.col-title{font-weight:300;font-size:19px;color:var(--ink);padding-bottom:4px;border-bottom:2px solid var(--green)}
.col-copy{font-weight:300;font-size:9.6px;line-height:1.3;color:var(--text)}
.col-copy p{margin-bottom:9px}
.col-rule{left:374px;top:590px;width:1px;height:235px;border-left:1px dotted #ccc}
.results{list-style:none}
.results li{position:relative;padding-left:11px;margin-bottom:6px}
.results li::before{content:"";position:absolute;left:0;top:3px;width:5px;height:5px;background:var(--orange)}
.results a{color:var(--green)}
.fine{font-size:7.5px;font-weight:400}

/* memberships */
.members-band{left:0;top:864px;width:749px;height:56px;background:var(--green);color:#fff;font-weight:500;font-size:28px;display:flex;align-items:center;justify-content:center;letter-spacing:.5px}
.members-pointer{left:366px;top:919px}
.members-body{left:0;top:920px;width:749px;height:185px;background:linear-gradient(180deg,#4a4a4a,#353535);text-align:center}
.member-strong{font-family:"Signika",sans-serif;font-weight:600;color:var(--orange);font-size:28px;line-height:34px}
.member-light{font-weight:300;color:#fff;font-size:21px;line-height:26px}

/* footer */
.site-footer{left:0;top:1105px;width:749px;height:95px;background:var(--footer)}
.footer-nav{left:76px;top:1136px;display:flex;font-size:8.5px;color:#ccc}
.footer-nav span{padding:0 11px;border-left:1px solid #555}
.footer-nav span:first-child{padding-left:0;border-left:none}
.footer-brand{left:557px;top:1124px;font-family:"Raleway",sans-serif;font-weight:800;font-size:22px;color:#666}
.footer-rule{left:0;top:1175px;width:749px;height:1px;background:#2a2a2a}
.copyright{left:0;top:1183px;width:749px;text-align:center;font-size:7.3px;color:#999}
.copyright b{color:#ccc;font-weight:500}
</style>
</head>
<body>

<header class="site-header abs"></header>
<div class="brand abs"><span class="brand-mark"></span><span class="brand-name">Veltrano, Inc.</span></div>

<div class="contact-line abs" style="left:418px">
  <svg width="16" height="16" viewBox="0 0 16 16"><path d="M3 2l3 0 1 4-2 1c1 2 2 3 4 4l1-2 4 1 0 3c0 1-1 2-2 2C7 15 1 9 1 4c0-1 1-2 2-2z" fill="#444"/></svg>
  (732) 555-0184
</div>
<div class="contact-divider abs"></div>
<div class="contact-line abs" style="left:551px">
  <svg width="16" height="18" viewBox="0 0 16 18"><rect x="2" y="4" width="12" height="13" rx="1" fill="#444"/><rect x="4" y="1" width="5" height="5" fill="#444"/><rect x="5" y="8" width="6" height="6" fill="#fff"/></svg>
  (732) 555-0197
</div>

<nav class="main-nav abs">
  <a class="current" href="#">Home</a>
  <a href="#">Our Company</a>
  <a href="#">Housing Rehab Application</a>
  <a href="#">Affordable Application</a>
  <a href="#">Contact Us</a>
</nav>

<section class="hero abs"></section>
<div class="hero-visual abs" role="img" aria-label="Photo of a hand drawing a business plan diagram with market research, business model and planning steps"></div>
<div class="hero-intro abs">Specializes In</div>
<div class="hero-line abs" style="left:77px;top:196px">COMMUNITY DEVELOPMENT</div>
<div class="hero-amp abs">&amp;</div>
<div class="hero-line abs" style="left:111px;top:226px">HOUSING REHABILITATION</div>
<div class="hero-sub abs">program planning, design and implementation</div>
<div class="cta abs">Connect With Us</div>

<div class="tile abs" style="left:75px" role="img" aria-label="Hands joined together in a circle on grass">Community<br>Development<br>Planning</div>
<div class="tile abs" style="left:225px" role="img" aria-label="Hands joined together in a circle on grass">Housing<br>Rehabilitation<br>Administration</div>
<div class="tile abs" style="left:375px" role="img" aria-label="Hands joined together in a circle on grass"><span style="font-size:12.5px;line-height:1.75">US Department of Housing<br>and Urban Development</span><small>(HUD)<br>Program Management</small></div>
<div class="tile abs" style="left:527px" role="img" aria-label="Hands joined together in a circle on grass"><span style="line-height:1.3">Implementation<br>of Programs</span><small>under the Jurisdiction of<br>New Jersey Council of<br>Affordable Housing (COAH)</small></div>

<section class="about abs"></section>
<div class="abs" style="left:75px;top:572px;width:293px">
  <h2 class="col-title" style="display:inline-block">Veltrano, Inc</h2>
  <div class="col-copy" style="margin-top:19px">
    <p>Is a city planning firm that specializes in community development and housing rehabilitation program planning, design and implementation. We have over twenty years of experience in developing and administering income base-base housing and programs in accordance with US Department of Housing and Urban Development (HUD) and New Jersey Council on Affordable Housing (COAH) rules and regulations,</p>
    <p>In addition, our firm is capable of providing the technical and administrative assistance our clients require for implementation of their income based housing programs. E. Martin Delacroix Associates is one of the most experience urban planning firms in New Jersey, with over forty years of as consulting planners.</p>
    <p class="fine" style="margin-top:14px;margin-bottom:2px">To find out more about federal housing programs that we will administer,</p>
    <p class="fine" style="color:var(--green)">please go to <b style="font-size:10.5px">www.fedhousingguide.org</b></p>
  </div>
</div>
<div class="col-rule abs"></div>
<div class="abs" style="left:390px;top:569px;width:300px">
  <h2 class="col-title" style="display:inline-block;padding-right:28px;padding-left:15px">We Get Results</h2>
  <ul class="results col-copy" style="margin-top:20px">
    <li>Veltrano designs income based programs to be supported by federal placement lotteries state funding</li>
    <li>We implement local programs to benefit people seeking access to affordable housing.</li>
    <li>Our experienced staff screen applicants for local affordable housing</li>
    <li>We pre-qualify persons who have applied for housing rehabilitation.<br><a href="#">Conduct placement lotteries</a></li>
    <li>Through local housing rehabilitation programs, our experience construction inspectors determine what improvements are required at eligible units based on local building codes and health and safety issues</li>
  </ul>
  <p class="fine" style="margin:10px 0 2px 8px">For more information about out services, please contact us today at</p>
  <p class="fine" style="margin-left:8px;font-size:8.5px"><b style="color:var(--ink);font-weight:500">VELTRANO</b> <span style="color:var(--green)">(732) 555-0184</span> or <i style="color:var(--green)">office@veltranoplanning.com</i></p>
</div>

<div class="members-band abs">MEMBERSHIPS</div>
<div class="members-body abs" role="img" aria-label="Faint city skyline behind membership list">
  <div style="padding-top:33px">
    <div class="member-strong">National Neighborhood Renewal Alliance</div>
    <div class="member-strong">Garden State Regional Planning Society</div>
    <div class="member-light" style="margin-top:6px">Shoreline Planning Officials Network Coastal Housing<br>and Development League</div>
  </div>
</div>
<svg class="members-pointer abs" width="18" height="9" viewBox="0 0 18 9"><path d="M0 0h18L9 9z" fill="var(--green)"/></svg>

<footer class="site-footer abs"></footer>
<div class="footer-nav abs">
  <span>Home</span><span>Our Company</span><span>Housing Rehab Application</span><span>Affordable Application</span><span>Contact Us</span>
</div>
<div class="footer-brand abs">Veltrano</div>
<div class="footer-rule abs"></div>
<div class="copyright abs">Copy Right 2014 Veltrano, 218 Harbor Point Road, Brick, New Jersey, 08724 &nbsp;<b>TEL (732) 555-0184 Fax (732) 555-0197</b></div>

</body>
</html>
```